Letterhead design for Sleep Consulting Business

I'm looking for a new letterhead (heading/footer) design for my Sleep Consulting Business, I work with families to help their children improve their sleep.

The heading/footer will used in Microsoft Word Only-to be used for all of my documents such as writing Sleep Plans. I need to utilize as much working space in the document as possible. This will NOT be printed out on paper- it will only be used for heading/footer on microsoft word, then emailed to clients, who may print it at home.

My brand colors:
Dark Blue Hex: 1F2A42
Lighter Blueish Hex: 90BEC9
You're welcome to check out my website for inspiration- it is freshly created with other colors as well, and I love the outcome. www.hollowpinerest.com

Target Market(s)

Tired parents

Font styles to use
Script
Other font styles liked:
• Great Vibe, Lato or Just Another Hand are all used currently for my brand. Open to other options.

Requirements
Must have
• The letterhead (heading/footer) MUST be kept narrow (height-wise), so I have plenty of space on my document, while including important information.

It should look professional on screen, and when printed.

Must include my business name OR logo (Hollow Pine Sleep Consulting), and my email address. Mara@hollowpinerest.com

Website is optional, not required, just if you need to fill in a spot: www.hollowpinerest.com

```html
<!DOCTYPE html>
<html lang="en">
<head>
<meta charset="utf-8">
<title>Hollow Pine Sleep Consulting – Letterhead</title>
<link rel="stylesheet" href="https://fonts.googleapis.com/css2?family=Lato:wght@400;700&display=swap">
<style>
  :root {
    --navy: #1F2A42;
    --mist: #90BEC9;
    --paper: #FFFFFF;
    --backdrop: #FFFFFF;
  }
  * { margin: 0; padding: 0; box-sizing: border-box; }
  html, body {
    width: 1200px;
    height: 1200px;
    overflow: hidden;
    background: var(--backdrop);
    font-family: "Lato", Arial, sans-serif;
  }
  .letterhead {
    position: absolute;
    left: 285px;
    top: 156px;
    width: 631px;
    height: 890px;
    background: var(--paper);
    border: 1px solid #ececec;
  }
  .brand {
    position: absolute;
    left: 48px;
    top: 44px;
    display: flex;
    align-items: center;
    gap: 12px;
  }
  .brand-mark {
    width: 55px;
    height: 55px;
    border-radius: 50%;
    background: var(--navy);
    flex: none;
  }
  .brand-name {
    color: var(--navy);
    font-weight: 400;
    line-height: 1.15;
  }
  .brand-name .primary {
    display: block;
    font-size: 24px;
  }
  .brand-name .secondary {
    display: block;
    font-size: 10px;
    letter-spacing: 2.2px;
    text-transform: uppercase;
    padding-left: 22px;
    margin-top: 3px;
  }
  .header-rule {
    position: absolute;
    left: 307px;
    right: 0;
    top: 90px;
    height: 3px;
    background: var(--mist);
  }
  .footer-band {
    position: absolute;
    left: 0;
    right: 0;
    top: 820px;
    height: 51px;
    background: var(--mist);
  }
  .contact {
    position: absolute;
    top: 0;
    height: 51px;
    display: flex;
    align-items: center;
    gap: 8px;
    color: var(--navy);
    font-size: 10.5px;
    font-weight: 700;
  }
  .contact svg { width: 13px; height: 13px; flex: none; }
  .contact-phone { left: 51px; }
  .contact-email { left: 191px; }
  .contact-web   { left: 404px; }
  .divider {
    position: absolute;
    top: 17px;
    width: 1.5px;
    height: 17px;
    background: var(--navy);
  }
  .divider-one { left: 164px; }
  .divider-two { left: 381px; }
</style>
</head>
<body>
  <main class="letterhead">
    <header>
      <div class="brand">
        <span class="brand-mark" aria-hidden="true"></span>
        <p class="brand-name">
          <span class="primary">Hollow Pine</span>
          <span class="secondary">Sleep Consulting</span>
        </p>
      </div>
      <div class="header-rule"></div>
    </header>

    <footer class="footer-band">
      <div class="contact contact-phone">
        <svg viewBox="0 0 24 24" aria-hidden="true"><path fill="#1F2A42" d="M6.6 10.8a15.1 15.1 0 0 0 6.6 6.6l2.2-2.2c.3-.3.7-.4 1-.2 1.1.4 2.3.6 3.6.6.6 0 1 .4 1 1V20c0 .6-.4 1-1 1C10.6 21 3 13.4 3 4c0-.6.4-1 1-1h3.5c.6 0 1 .4 1 1 0 1.3.2 2.5.6 3.6.1.3 0 .7-.2 1z"/></svg>
        <span>555-208-3147</span>
      </div>
      <span class="divider divider-one"></span>
      <div class="contact contact-email">
        <svg viewBox="0 0 24 24" aria-hidden="true"><rect x="2" y="5" width="20" height="14" rx="1.5" fill="#1F2A42"/><path d="M3 6.5l9 6.5 9-6.5" fill="none" stroke="#90BEC9" stroke-width="1.6"/></svg>
        <span>Mara@hollowpinerest.com</span>
      </div>
      <span class="divider divider-two"></span>
      <div class="contact contact-web">
        <svg viewBox="0 0 24 24" aria-hidden="true"><g fill="none" stroke="#1F2A42" stroke-width="2"><circle cx="12" cy="12" r="9.5"/><ellipse cx="12" cy="12" rx="4" ry="9.5"/><path d="M2.5 12h19M4 7h16M4 17h16"/></g></svg>
        <span>www.hollowpinerest.com</span>
      </div>
    </footer>
  </main>
</body>
</html>
```